依頼概要
■ 依頼の目的/概要

弊社は「カード選びナビ広場 http://www.hoshizora-cardnavi.com/ 」というクレジットカードの比較サイトを運営しています。
今回はこのカード選びナビ広場のトップページのサイトデザインリニューアルをお願いします。

現在、サイト内( http://www.hoshizora-cardnavi.com/ )にある素材は自由に使って頂いて構いません。
既存のデザインを残しつつデザインをしていただいても
逆に完全新規にデザインをしていただいても構いません。
最終的なクオリティが高ければOKです。
素材サイトで何か素材を購入すればよりクオリティが高くなるのであれば
別途素材の購入も検討します。
その際はメッセージでご連絡ください。

■コーディング不要
コーディングは不要なので、デザインのみでOKです。

■ 希望するウェブデザイン

サイト訪問者が楽しくクレジットカードを選んだり
クレジットカードについての知識を学んだりできるようなデザインが希望です。
逆にサイト訪問者が堅苦しく感じてしまうようなデザインは避けたいです。
既存サイトでは下記URLのようなサイトデザインが好みです。

http://www.mz.tobira-net.com/mobile/index.html?bid=mz_gn_0007
http://www.mirumart.co.jp/kuruma/index.html?ca=top_glo_009
http://store.fenlow.com/jp/
http://store.tavix.jp/Special/Compare/Computer/Relmo/index.html

また「クレジットカード」で検索して1ページ目に出てくるサイトには
綺麗なサイトが多いので、こちらも参考にして頂きたいです。

【サイズの横幅について】

現在の横幅はぴったり950pxですが、
980px前後までであれば、横幅が大きくなっても構いません。
横幅が現在よりも小さくなるのは不可です。

ただし、ヘッダー部分とフッター部分は下記サイトのように横全体に広がっているデザインが希望です。
http://www.qrt.co.jp/ordercard/index.html

■ 納品ファイルの希望

第一希望 フォトショップ形式 + BMP形式
第二希望 イラストレーター形式 + BMP形式

■ 進め方

弊社の希望するイメージに近い提案を1つ(場合によって複数)選択させて頂きます。希望に近づけるために、修正要望を個別にさせて頂くこともあります。コンペ方式のため、修正後に当選されない場合も、どうかご了承ください。

■ その他/注意点

選択させて頂いたウェブデザインの著作権(財産権)等の扱いはTezukuri利用規約に従い、弊社に譲渡をお願いします。フォントや画像素材などを利用する場合は上記利用用途に使用できることを確認し、第三者の知的財産権等に注意して下さい。
■リニューアルによる変更点
今回のリニューアルではデザイン面だけでなくシステム面も強化するため
トップページのデザインが一部変更になります。
変更点は添付ファイルにまとめました。
なので現在のトップページのデザイン( http://www.hoshizora-cardnavi.com/
ではなく添付ファイル内のデザインを元にデザインをしてください。

```html
<!DOCTYPE html>
<html lang="ja">
<head>
<meta charset="utf-8">
<title>カード選びナビ広場</title>
<link rel="stylesheet" href="https://fonts.googleapis.com/css2?family=Noto+Sans+JP:wght@400;700&display=swap">
<style>
:root{
  --ink:#333;
  --muted:#777;
  --line:#d6d6d6;
  --panel:#f4f4f4;
  --blue:#1f5fa8;
  --blue-soft:#e8f1fb;
  --orange:#f08a00;
  --red:#d9342b;
  --green:#4a9a2e;
  --dark:#3a3a3a;
  --nav-top:#fdfdfd;
  --nav-bot:#dcdcdc;
}
*{box-sizing:border-box;margin:0;padding:0}
html,body{width:1200px;height:2800px;overflow:hidden}
body{font-family:"Noto Sans JP",sans-serif;font-size:12px;color:var(--ink);background:#fff;line-height:1.5}
.wrap{width:980px;margin:0 auto;position:relative}
/* header */
.site-header{height:70px;border-bottom:1px solid var(--line)}
.site-header .wrap{display:flex;align-items:center;height:70px;gap:18px}
.brand{display:flex;align-items:center;gap:8px;font-size:22px;font-weight:700;color:var(--blue)}
.brand-mark{width:22px;height:22px;border-radius:50%;background:var(--orange)}
.tagline{font-size:15px;color:var(--ink)}
.tagline small{font-size:11px;color:var(--muted)}
.header-note{margin-left:auto;font-size:11px;color:var(--muted)}
.global-nav{height:40px;background:linear-gradient(var(--nav-top),var(--nav-bot));border-bottom:1px solid #bbb}
.global-nav ul{display:flex;list-style:none;height:40px}
.global-nav li{flex:1;display:flex;align-items:center;justify-content:center;font-size:13px;font-weight:700;border-right:1px solid #c4c4c4}
.global-nav li:first-child{border-left:1px solid #c4c4c4}
.global-nav li.wide{flex:2}
/* columns */
.page{display:flex;gap:15px;margin-top:12px}
.main{width:730px}
.side{width:235px}
.box{border:1px solid var(--line);margin-bottom:14px;background:#fff}
.box-title{height:32px;display:flex;align-items:center;gap:8px;padding:0 10px;background:linear-gradient(#fafafa,#e9e9e9);border-bottom:1px solid var(--line);font-weight:700;font-size:13px}
.box-title::before{content:"";width:6px;height:16px;background:var(--blue)}
.intro{padding:12px 14px;font-size:12px;height:72px}
.intro em{color:var(--red);font-style:normal}
.news li{list-style:none;display:flex;gap:10px;padding:6px 12px;border-bottom:1px dotted var(--line);font-size:11px}
.news .date{color:var(--muted)}
.news .tag{background:var(--green);color:#fff;padding:0 6px;font-size:10px}
/* lineup */
.lineup{display:grid;grid-template-columns:repeat(4,1fr);gap:10px;padding:12px}
.lineup .pick{font-size:11px}
.pick .label{color:var(--blue);font-weight:700}
.pick .price{font-size:12px;font-weight:700}
.card-img{height:82px;border-radius:6px;margin:6px 0;background:linear-gradient(135deg,#2c6fb8,#9cc6ec)}
.card-img.red{background:linear-gradient(135deg,#c43b3b,#f3a2a2)}
.card-img.gold{background:linear-gradient(135deg,#a88a3c,#f0dea0)}
.card-img.dark{background:linear-gradient(135deg,#333,#8b8b8b)}
.pick p{color:var(--muted);font-size:10px;height:60px}
.banners{display:flex;gap:10px;padding:12px}
.banner{flex:1;height:62px;border-radius:6px;background:linear-gradient(#fff6e0,#ffe2a8);border:1px solid #f0c878;display:flex;align-items:center;gap:10px;padding:0 10px;font-size:12px;font-weight:700}
.mascot{width:44px;height:44px;border-radius:6px;background:#f7d36a}
/* features */
.features{display:grid;grid-template-columns:repeat(3,1fr);gap:14px;padding:14px}
.feature{border:1px solid var(--line)}
.feature .photo{height:80px;background:linear-gradient(#9fc7e8,#e6f1fa)}
.feature .photo.warm{background:linear-gradient(#e8d7a8,#fbf2d8)}
.feature h3{font-size:12px;color:var(--blue);padding:6px 8px 2px}
.feature p{font-size:10px;color:var(--muted);padding:0 8px 8px;height:40px}
/* search */
.search-head{height:34px;display:flex;align-items:center;padding:0 12px;background:var(--dark);color:#fff;font-weight:700;font-size:13px}
.search{padding:12px 16px}
.group{margin-bottom:14px}
.group h4{font-size:12px;border-bottom:1px solid var(--line);padding-bottom:3px;margin-bottom:6px}
.checks{display:grid;grid-template-columns:repeat(3,1fr);gap:5px 12px;font-size:11px}
.checks span{display:flex;align-items:center;gap:5px}
.checks span::before{content:"";width:10px;height:10px;border:1px solid #999;background:#fff}
.select{display:inline-block;width:160px;height:22px;border:1px solid #aaa;font-size:11px;padding:2px 6px}
.search-go{display:flex;justify-content:center;gap:20px;align-items:center;padding:16px 0 4px}
.btn{display:inline-flex;align-items:center;justify-content:center;height:34px;padding:0 26px;border-radius:17px;background:linear-gradient(#5b9be0,var(--blue));color:#fff;font-weight:700;font-size:13px}
.btn.ghost{background:#eee;color:var(--ink);border:1px solid #bbb}
.more-link{text-align:center;font-size:11px;color:var(--blue);margin:10px 0 16px}
/* compare */
.compare{display:grid;grid-template-columns:1fr 1fr;gap:16px;padding:16px}
.vs-box{border:1px solid var(--line)}
.vs-box h3{font-size:12px;background:var(--blue-soft);padding:5px 8px;color:var(--blue)}
.vs-row{display:flex;align-items:center;justify-content:space-between;padding:18px 14px}
.vs-row .card-img{width:130px;height:84px;margin:0}
.vs{font-size:20px;font-weight:700;color:var(--red)}
.vs-box p{font-size:10px;color:var(--muted);padding:0 12px 12px}
/* sidebar */
.promo{height:130px;background:linear-gradient(135deg,#2d2d2d,#6c6c6c);color:#fff;padding:14px;font-weight:700;font-size:14px;display:flex;flex-direction:column;justify-content:space-between}
.promo .card-img{width:110px;height:66px;margin:0;align-self:flex-end}
.side-list li{list-style:none;display:flex;align-items:center;gap:8px;padding:7px 10px;border-bottom:1px dotted var(--line);font-size:11px;color:var(--blue)}
.side-list li::before{content:"";width:8px;height:8px;background:var(--orange);border-radius:50%}
.brand-row{display:grid;grid-template-columns:1fr 1fr;gap:6px;padding:10px}
.brand-row span{height:34px;border:1px solid var(--line);display:flex;align-items:center;justify-content:center;font-size:11px;font-weight:700;color:var(--blue)}
.ad{height:150px;background:linear-gradient(#e9f3fd,#fff);border:1px solid #bcd6f0;padding:12px;text-align:center}
.ad .lead{color:var(--red);font-weight:700;font-size:14px}
.ad .name{font-size:22px;font-weight:700;color:var(--blue);margin:6px 0}
.ad .cta{display:inline-block;background:var(--orange);color:#fff;padding:3px 14px;border-radius:3px;font-size:11px;font-weight:700}
.side-gold{height:120px;background:linear-gradient(135deg,#8a6d25,#e8d08a);margin-bottom:14px}
.side-text{padding:10px;font-size:10px;color:var(--muted)}
/* footer */
.site-footer{position:absolute;left:0;right:0;top:2540px;height:260px;background:#f1f1f1;border-top:3px solid var(--blue)}
.footer-links{display:grid;grid-template-columns:repeat(4,1fr);gap:8px 20px;padding:26px 0 20px;font-size:11px;color:var(--blue)}
.footer-about{font-size:11px;color:var(--muted);width:620px}
.copyright{position:absolute;left:0;right:0;bottom:0;height:48px;background:var(--dark);color:#ddd;font-size:11px;display:flex;align-items:center;justify-content:center}
.pagetop{position:absolute;right:0;top:24px;background:#fff;border:1px solid var(--line);padding:3px 12px;font-size:11px}
</style>
</head>
<body>
<header class="site-header">
  <div class="wrap">
    <div class="brand"><span class="brand-mark"></span>カード選びナビ広場</div>
    <div class="tagline">ライフスタイルにあった1枚を <small>クレジットカードを比較して選ぼう</small></div>
    <div class="header-note">初めての方へ ｜ サイトマップ</div>
  </div>
</header>
<nav class="global-nav">
  <div class="wrap">
    <ul><li>カードの比較と選び方</li><li>人気カードを比較</li><li>一覧表で比較</li><li>ブログ</li><li class="wide">カード選びナビ広場とは</li></ul>
  </div>
</nav>

<div class="wrap page">
  <main class="main">
    <section class="box intro">
      <p>カード選びナビ広場ではあなたにぴったりのクレジットカードを探せます。</p>
      <p>年会費・ポイント・特典などの条件から、<em>目的別にカードを比較して選ぶことができます。</em></p>
      <p>初めてカードを作る方も、気軽に知識を学んでいってください。</p>
    </section>

    <section class="box">
      <h2 class="box-title">新着情報</h2>
      <ul class="news">
        <li><span class="date">2012.08.03</span><span class="tag">更新</span>ゴールドカードの特集ページを追加しました</li>
        <li><span class="date">2012.08.01</span><span class="tag">更新</span>人気カードの比較表を新しい情報に更新しました</li>
        <li><span class="date">2012.07.27</span><span class="tag">更新</span>ポイント還元率の高いカード一覧を更新しました</li>
        <li><span class="date">2012.07.20</span><span class="tag">更新</span>海外旅行保険つきカードの記事を公開しました</li>
        <li><span class="date">2012.07.12</span><span class="tag">更新</span>学生向けカードの選び方をまとめました</li>
      </ul>
    </section>

    <section class="box">
      <h2 class="box-title">今月のおすすめカード</h2>
      <div class="lineup">
        <div class="pick"><div class="label">年会費無料</div><div class="price">初年度0円</div><div class="card-img"></div><p>毎日の買い物でポイントが貯まりやすい定番の一枚です。</p></div>
        <div class="pick"><div class="label">ポイント重視</div><div class="price">還元率1.5%</div><div class="card-img red"></div><p>ネット通販での利用でポイントが大きく増えるカードです。</p></div>
        <div class="pick"><div class="label">旅行に強い</div><div class="price">年会費2,000円</div><div class="card-img gold"></div><p>海外旅行保険とマイル特典が充実したカードです。</p></div>
        <div class="pick"><div class="label">ステータス</div><div class="price">年会費10,000円</div><div class="card-img dark"></div><p>空港ラウンジなど上質なサービスを受けられます。</p></div>
      </div>
      <div class="banners">
        <div class="banner"><span class="mascot" role="img" aria-label="案内役のキャラクター"></span>はじめてのカード選びガイド</div>
        <div class="banner"><span class="mascot" role="img" aria-label="案内役のキャラクター"></span>カード診断で相性チェック</div>
      </div>
    </section>

    <section class="box">
      <h2 class="box-title">目的別でカードを選ぶ</h2>
      <div class="features">
        <div class="feature"><div class="photo" role="img" aria-label="旅行の風景写真"></div><h3>旅行・マイル</h3><p>旅先で役立つ保険やマイル特典で選ぶ。</p></div>
        <div class="feature"><div class="photo warm" role="img" aria-label="買い物の写真"></div><h3>ポイント還元</h3><p>還元率の高さでお得なカードを選ぶ。</p></div>
        <div class="feature"><div class="photo" role="img" aria-label="セキュリティの写真"></div><h3>安心・補償</h3><p>不正利用の補償が手厚いカードを選ぶ。</p></div>
        <div class="feature"><div class="photo warm" role="img" aria-label="街の写真"></div><h3>年会費無料</h3><p>維持費をかけずに持てるカードを選ぶ。</p></div>
        <div class="feature"><div class="photo" role="img" aria-label="オフィスの写真"></div><h3>法人・ビジネス</h3><p>経費管理に便利なカードを選ぶ。</p></div>
        <div class="feature"><div class="photo warm" role="img" aria-label="学生生活の写真"></div><h3>学生・新社会人</h3><p>初めてでも作りやすいカードを選ぶ。</p></div>
      </div>
    </section>

    <section class="box">
      <h2 class="search-head">条件からクレジットカードを検索</h2>
      <div class="search">
        <div class="group"><h4>カード・特典</h4>
          <div class="checks"><span>ポイント還元率が高い</span><span>マイルが貯まる</span><span>海外旅行保険つき</span><span>国内旅行保険つき</span><span>ショッピング保険</span><span>電子マネー対応</span><span>ETCカード発行可</span><span>家族カード発行可</span><span>即日発行</span></div>
        </div>
        <div class="group"><h4>年会費</h4>
          <div class="checks"><span>永年無料</span><span>初年度無料</span><span>条件つき無料</span><span>5,000円以下</span><span>10,000円以下</span><span>10,000円以上</span></div>
        </div>
        <div class="group"><h4>カードの種類</h4>
          <div class="checks"><span>一般カード</span><span>ゴールドカード</span><span>プラチナカード</span><span>学生カード</span><span>法人カード</span><span>提携カード</span></div>
        </div>
        <div class="group"><h4>国際ブランド</h4>
          <div class="checks"><span>カードA</span><span>カードB</span><span>カードC</span><span>カードD</span><span>カードE</span><span>こだわらない</span></div>
        </div>
        <div class="group"><h4>ポイント</h4>
          <div class="checks"><span>有効期限なし</span><span>他社ポイントへ移行可</span><span>商品券に交換可</span></div>
        </div>
        <div class="group"><h4>キーワード</h4><span class="select">選択してください ▼</span></div>
        <div class="group"><h4>発行会社</h4>
          <div class="checks"><span>銀行系</span><span>信販系</span><span>流通系</span><span>交通系</span><span>通信系</span><span>その他</span></div>
        </div>
        <div class="search-go"><span class="btn">この条件で検索する</span><span class="btn ghost">条件をクリア</span></div>
      </div>
    </section>
    <p class="more-link">カード一覧表はこちら ›</p>

    <section class="box">
      <h2 class="box-title">人気カードを比較</h2>
      <div class="compare">
        <div class="vs-box"><h3>スタンダードカード対決</h3><div class="vs-row"><div class="card-img"></div><span class="vs">VS</span><div class="card-img red"></div></div><p>年会費無料の人気カード同士を徹底比較します。</p></div>
        <div class="vs-box"><h3>ポイント重視カード対決</h3><div class="vs-row"><div class="card-img red"></div><span class="vs">VS</span><div class="card-img"></div></div><p>還元率と使いやすさで二枚を比べます。</p></div>
        <div class="vs-box"><h3>ゴールドカード対決</h3><div class="vs-row"><div class="card-img gold"></div><span class="vs">VS</span><div class="card-img gold"></div></div><p>特典とサービスの違いをわかりやすく解説します。</p></div>
        <div class="vs-box"><h3>ステータスカード対決</h3><div class="vs-row"><div class="card-img dark"></div><span class="vs">VS</span><div class="card-img gold"></div></div><p>上位カードの付帯サービスを比較します。</p></div>
      </div>
    </section>
  </main>

  <aside class="side">
    <div class="box promo"><span>今月の注目カード</span><div class="card-img gold"></div></div>
    <ul class="box side-list">
      <li>初めての方へ</li><li>カードの選び方</li><li>年会費無料カード</li><li>ポイント比較</li><li>マイル比較</li><li>ゴールドカード比較</li><li>学生向けカード</li><li>カード用語集</li><li>よくある質問</li>
    </ul>
    <div class="box"><h2 class="box-title">国際ブランド</h2><div class="brand-row"><span>カードA</span><span>カードB</span><span>カードC</span><span>カードD</span></div></div>
    <div class="box ad"><p class="lead">ポイント3倍</p><p class="name">ミライプラス</p><p>入会特典キャンペーン実施中</p><p style="margin-top:8px"><span class="cta">詳細はこちら</span></p></div>
    <div class="box"><h2 class="box-title">ゴールドカード特集</h2><div class="side-gold"></div><p class="side-text">人気のゴールドカードを特典別に紹介しています。</p></div>
    <div class="box"><h2 class="box-title">ブログ新着</h2>
      <ul class="side-list"><li>ポイントの上手な貯め方</li><li>旅行保険の基礎知識</li><li>年会費の元を取るコツ</li><li>カードの安全な使い方</li><li>審査に関する基礎知識</li></ul>
    </div>
  </aside>
</div>

<footer class="site-footer">
  <div class="wrap">
    <div class="footer-links">
      <span>カードの比較と選び方</span><span>人気カードを比較</span><span>一覧表で比較</span><span>ブログ</span>
      <span>初めての方へ</span><span>運営者情報</span><span>プライバシーポリシー</span><span>お問い合わせ</span>
    </div>
    <p class="footer-about">カード選びナビ広場は、クレジットカードの特典や年会費を比較して、あなたに合った一枚を見つけるための情報サイトです。掲載情報は各社の公式情報をもとに作成しています。</p>
    <span class="pagetop">ページの先頭へ</span>
  </div>
  <div class="copyright">Copyright © カード選びナビ広場 All Right Reserved.</div>
</footer>
</body>
</html>
```